Business Card Design

​Silver Harbor Grooves provides personal, friendly service in a fun and high energy environment. We are based in Vermont.

We would like a card that appeals to a wide range of audiences as we do a wide range of events. Please feel free to check out our website silverharborgrooves.com for inspiration.

Target Market(s)

weddings, corporate, birthday parties, colleges

Industry/Entity Type

Business

Contact Information for Business Card

Silver Harbor Grooves
Providing Entertainment For All Occasions
555 218 6093
silverharborgrooves@mailvane.com
silverharborgrooves.com

```html
<!DOCTYPE html>
<html lang="en">
<head>
<meta charset="utf-8">
<title>Silver Harbor Grooves – Business Card</title>
<link rel="stylesheet" href="https://fonts.googleapis.com/css2?family=Open+Sans:wght@400;600;700&display=swap">
<style>
  :root {
    --page-bg: #ececec;
    --card-bg: #ffffff;
    --green-dark: #1f3b12;
    --green-mid: #3e6d24;
    --text-grey: #444444;
    --divider: #c9c9c9;
    --white: #ffffff;
  }
  * { box-sizing: border-box; margin: 0; padding: 0; }
  html, body {
    width: 1200px; height: 1200px; overflow: hidden;
    background: var(--page-bg);
    font-family: "Open Sans", Arial, sans-serif;
  }
  .sheet {
    width: 1200px; height: 1200px;
    display: flex; flex-direction: column; align-items: center; justify-content: center;
    gap: 60px;
  }
  .card {
    position: relative;
    width: 900px; height: 514px;
    background: var(--card-bg);
    border-radius: 26px;
    overflow: hidden;
    box-shadow: 0 4px 14px rgba(0,0,0,0.12);
  }
  /* Front */
  .front-brand {
    position: absolute; left: 50px; top: 150px; width: 330px;
    text-align: center;
    color: var(--green-dark);
    font-weight: 700; font-size: 38px; line-height: 1.15;
    letter-spacing: 0.5px; text-transform: uppercase;
  }
  .divider {
    position: absolute; left: 412px; top: 58px;
    width: 2px; height: 230px; background: var(--divider);
  }
  .contact {
    position: absolute; left: 440px; top: 54px;
    color: var(--text-grey); font-size: 20px;
  }
  .contact .person-name { color: var(--green-dark); font-weight: 700; font-size: 30px; line-height: 1.2; }
  .contact .person-title { font-weight: 600; font-size: 21px; margin-bottom: 22px; }
  .contact .line { display: flex; align-items: center; gap: 8px; margin-bottom: 12px; }
  .contact .line svg { width: 18px; height: 18px; flex: none; }
  .contact .address { margin-top: 22px; line-height: 1.7; }
  .swoosh { position: absolute; left: 0; bottom: 0; width: 900px; height: 514px; }
  .front-url {
    position: absolute; left: 0; right: 0; bottom: 26px;
    text-align: center; color: var(--white);
    font-size: 24px; font-weight: 600; letter-spacing: 1px;
  }
  /* Back */
  .back-brand {
    position: absolute; left: 0; right: 0; top: 170px;
    text-align: center; color: var(--green-dark);
    font-weight: 700; font-size: 62px; letter-spacing: 1px;
    text-transform: uppercase;
  }
  .back-url {
    position: absolute; left: 0; right: 0; top: 400px;
    text-align: center; color: var(--text-grey);
    font-size: 27px; font-weight: 600; letter-spacing: 1px;
  }
</style>
</head>
<body>
<main class="sheet">
  <section class="card card-front">
    <div class="front-brand">Silver Harbor<br>Grooves</div>
    <div class="divider"></div>
    <div class="contact">
      <p class="person-name">Your Name</p>
      <p class="person-title">Title</p>
      <p class="line">
        <svg viewBox="0 0 20 20" aria-hidden="true"><circle cx="10" cy="10" r="10" fill="var(--green-dark)"/><path d="M6.5 5.5l2 2-1 1.2c.7 1.4 1.6 2.3 3 3l1.2-1 2 2-1.2 1.5c-3.5-.3-6.5-3.3-7-7z" fill="#fff"/></svg>
        555 218 6093
      </p>
      <p class="line">
        <svg viewBox="0 0 20 20" aria-hidden="true"><circle cx="10" cy="10" r="10" fill="var(--green-dark)"/><rect x="5" y="6.5" width="10" height="7" fill="#fff"/><path d="M5 6.5l5 4 5-4" stroke="var(--green-dark)" stroke-width="1.2" fill="none"/></svg>
        silverharborgrooves@mailvane.com
      </p>
      <p class="address">Sreet Name, City Name<br>Zip Code-00000</p>
    </div>
    <svg class="swoosh" viewBox="0 0 900 514" aria-hidden="true">
      <path d="M0 380 Q 420 300 900 352" stroke="var(--green-mid)" stroke-width="8" fill="none"/>
      <path d="M0 408 Q 430 330 900 378 L900 514 L0 514 Z" fill="var(--green-dark)"/>
    </svg>
    <p class="front-url">www.silverharborgrooves.com</p>
  </section>

  <section class="card card-back">
    <div class="back-brand">Silver Harbor Grooves</div>
    <p class="back-url">www.silverharborgrooves.com</p>
  </section>
</main>
</body>
</html>
```